Bookmark Design

We would like to design a book mark with logos of our two business and a quote.

One side with the quote "The first wealth is health" - Tobias Quill Harrow and the two logos.

The back side has the two logos with its respective phone numbers and a common address (this is to be advised to the winner of the project).

```html
<!DOCTYPE html>
<html lang="en">
<head>
<meta charset="UTF-8">
<title>Bookmark – Front and Back</title>
<link rel="stylesheet" href="https://fonts.googleapis.com/css2?family=Archivo:ital,wght@1,800;1,900&family=Inter:wght@400;600;700&display=swap">
<style>
  :root {
    --canvas-grey: #5f5f5f;
    --paper: #ffffff;
    --teal: #2a6275;
    --sun: #ede36c;
    --quote-red: #e8324a;
    --author-grey: #555555;
    --ink: #1e1e1e;
    --clinic-navy: #27489a;
    --dental-green: #6fae5a;
    --photo-top: #d9e25a;
    --photo-bottom: #b7c0c6;
  }
  * { margin: 0; padding: 0; box-sizing: border-box; }
  html, body { width: 920px; height: 1200px; overflow: hidden; }
  body { background: var(--canvas-grey); position: relative; font-family: "Inter", sans-serif; }

  .bookmark {
    position: absolute;
    top: 65px;
    width: 309px;
    height: 1080px;
    background: var(--paper);
    overflow: hidden;
  }
  .bookmark--front { left: 88px; outline: 1px solid #222; }
  .bookmark--back { left: 515px; outline: 1px solid #888; }

  .hero-photo {
    position: absolute;
    left: 0; top: 0;
    width: 100%; height: 197px;
    background: linear-gradient(180deg, var(--photo-top) 0%, #c9d352 55%, var(--photo-bottom) 100%);
  }
  .bands { position: absolute; left: 0; top: 0; width: 309px; height: 1080px; }

  .quote {
    position: absolute;
    left: 0; top: 310px;
    width: 100%;
    text-align: center;
    font-family: "Archivo", sans-serif;
    font-style: italic;
    font-weight: 900;
    color: var(--teal);
    font-size: 54px;
    line-height: 63px;
    letter-spacing: -1px;
  }
  .quote__line { display: block; position: relative; }
  .quote__mark {
    position: absolute;
    color: var(--quote-red);
    font-size: 52px;
    line-height: 1;
  }
  .quote__mark--open { left: 52px; top: -8px; }
  .quote__mark--close { right: 20px; top: -12px; }

  .quote__author {
    position: absolute;
    left: 0; top: 640px;
    width: 100%;
    text-align: center;
    padding-left: 36px;
    font-family: "Archivo", sans-serif;
    font-style: italic;
    font-weight: 800;
    font-size: 18px;
    color: var(--author-grey);
  }

  .brand {
    position: absolute;
    left: 0;
    width: 100%;
    display: flex;
    flex-direction: column;
    align-items: center;
    gap: 10px;
    font-family: "Inter", sans-serif;
    font-weight: 700;
    font-size: 19px;
    line-height: 1.15;
    text-align: center;
  }
  .brand__dot { width: 54px; height: 54px; border-radius: 50%; }
  .brand__square { width: 30px; height: 30px; }
  .brand--clinic { color: var(--clinic-navy); }
  .brand--clinic .brand__dot { border: 3px solid var(--clinic-navy); }
  .brand--dental { color: var(--dental-green); }
  .brand--dental .brand__square { background: var(--dental-green); }

  .bookmark--front .brand--clinic { top: 735px; }
  .bookmark--front .brand--dental { top: 900px; }
  .bookmark--back .brand--clinic { top: 346px; }
  .bookmark--back .brand--dental { top: 700px; }

  .blurb {
    position: absolute;
    left: 0;
    width: 100%;
    padding: 0 58px;
    text-align: center;
    font-size: 13.5px;
    line-height: 25px;
    color: var(--ink);
  }
  .blurb--clinic { top: 489px; }
  .blurb--dental { top: 812px; }

  .divider {
    position: absolute;
    left: 117px; top: 629px;
    width: 75px; height: 4px;
    background: var(--sun);
  }
</style>
</head>
<body>

  <section class="bookmark bookmark--front">
    <div class="hero-photo" role="img" aria-label="Photo of a hand turning letter dice from wealth to health beside stacked coins and a red apple"></div>
    <svg class="bands" viewBox="0 0 309 1080" aria-hidden="true">
      <polygon points="0,197 309,197 309,221 0,249" fill="var(--teal)"/>
      <polygon points="0,258 309,229 309,245 0,289" fill="var(--sun)"/>
      <polygon points="0,1033 309,990 309,1020 0,1050" fill="var(--sun)"/>
      <polygon points="0,1054 309,1028 309,1080 0,1080" fill="var(--teal)"/>
    </svg>

    <blockquote class="quote">
      <span class="quote__line">The<span class="quote__mark quote__mark--open">“</span></span>
      <span class="quote__line">First</span>
      <span class="quote__line">Wealth</span>
      <span class="quote__line">is</span>
      <span class="quote__line">Health<span class="quote__mark quote__mark--close">”</span></span>
    </blockquote>
    <p class="quote__author">- Tobias Quill Harrow</p>

    <div class="brand brand--clinic">
      <span class="brand__dot"></span>
      <span class="brand__name">NORTHBROOK<br>CLINIC</span>
    </div>
    <div class="brand brand--dental">
      <span class="brand__square"></span>
      <span class="brand__name">Harbour Dental<br>Northbrook</span>
    </div>
  </section>

  <section class="bookmark bookmark--back">
    <div class="hero-photo" role="img" aria-label="Photo of a hand turning letter dice from wealth to health beside stacked coins and a red apple"></div>
    <svg class="bands" viewBox="0 0 309 1080" aria-hidden="true">
      <polygon points="0,197 309,197 309,221 0,249" fill="var(--teal)"/>
      <polygon points="0,258 309,229 309,245 0,289" fill="var(--sun)"/>
      <polygon points="0,1033 309,990 309,1020 0,1050" fill="var(--sun)"/>
      <polygon points="0,1054 309,1028 309,1080 0,1080" fill="var(--teal)"/>
    </svg>

    <div class="brand brand--clinic">
      <span class="brand__dot"></span>
      <span class="brand__name">NORTHBROOK<br>CLINIC</span>
    </div>
    <p class="blurb blurb--clinic">Ut wisi enim ad minim veniam, quis nostrud exerci tation ullamcorper suscipit lobortis.</p>

    <div class="divider"></div>

    <div class="brand brand--dental">
      <span class="brand__square"></span>
      <span class="brand__name">Harbour Dental<br>Northbrook</span>
    </div>
    <p class="blurb blurb--dental">Ut wisi enim ad minim veniam, quis nostrud exerci tation ullamcorper suscipit lobortis.</p>
  </section>

</body>
</html>
```